Business Card Design for Venture Kite

Venture Kite is a pro bono student consultancy service offered by Corvala KTRB to social start ups and enterprises. We provide consulting services with expertise in areas such as Marketing, IT, Business Strategy and Innovation.
I have attached\ the Venture Kite Logo here for your perusal.
Industry/Entity Type
Business
Contact Information for Business Card
Name: Ha Min Park Name: Thomas Leung
Role: Project Leader Role: Vice Project Leader
M:0477203941 M: 0479352806
E: ha-min.park@corvalaktrb.org E: thomas.leung@corvalaktrb.org
W: www.corvalaktrb.org W: www.corvalaktrb.org

```html
<!DOCTYPE html>
<html lang="en">
<head>
<meta charset="utf-8">
<title>Venture Kite — Business Cards</title>
<link rel="stylesheet" href="https://fonts.googleapis.com/css2?family=Ubuntu:ital,wght@0,400;0,700;1,400;1,700&display=swap">
<style>
  :root {
    --backdrop: #d6d6d4;
    --card: #f7f7f5;
    --orange: #d98a1f;
    --ink: #1c1c1c;
    --faint: #c9c9c9;
    --on-orange: #ffffff;
  }
  * { margin: 0; padding: 0; box-sizing: border-box; }
  html, body {
    width: 1200px; height: 1000px; overflow: hidden;
    background: var(--backdrop);
    font-family: "Ubuntu", sans-serif;
  }
  .sheet {
    position: relative; width: 1200px; height: 1000px;
    display: flex; flex-direction: column; align-items: center; justify-content: center; gap: 44px;
  }
  .card {
    position: relative; width: 760px; height: 434px;
    background: var(--card);
    box-shadow: 0 6px 18px rgba(0,0,0,0.18);
    overflow: hidden;
  }
  .card-shapes { position: absolute; inset: 0; width: 100%; height: 100%; }
  .card-shapes .band { fill: var(--orange); }

  .brand {
    position: absolute;
    font-weight: 700; text-transform: uppercase; letter-spacing: 0.02em;
    line-height: 1;
  }
  .brand--main { left: 0; right: 0; top: 178px; text-align: center; font-size: 52px; color: var(--ink); }
  .brand--faint-top { left: 46px; top: 48px; font-size: 40px; color: var(--faint); }
  .brand--faint-bottom { right: 46px; bottom: 46px; font-size: 40px; color: var(--faint); }

  .contact { position: absolute; color: var(--on-orange); }
  .contact--primary { right: 44px; top: 58px; text-align: right; }
  .contact--secondary { left: 44px; top: 246px; text-align: left; }
  .contact-name { font-weight: 700; font-style: italic; font-size: 25px; }
  .contact-role { font-style: italic; font-size: 18px; margin-bottom: 16px; }
  .contact--secondary .contact-role { font-style: normal; font-size: 17px; }
  .contact-line { font-size: 18px; line-height: 1.5; }
</style>
</head>
<body>
<main class="sheet">

  <section class="card card--front" aria-label="Card front">
    <svg class="card-shapes" viewBox="0 0 760 434" preserveAspectRatio="none" aria-hidden="true">
      <polygon class="band" points="0,0 540,0 500,32 0,32"/>
      <polygon class="band" points="300,392 760,392 760,434 255,434"/>
    </svg>
    <div class="brand brand--main">Venture Kite</div>
  </section>

  <section class="card card--back" aria-label="Card back">
    <svg class="card-shapes" viewBox="0 0 760 434" preserveAspectRatio="none" aria-hidden="true">
      <polygon class="band" points="0,174 198,204 380,0 760,0 760,269 547,239 251,434 0,434"/>
    </svg>
    <div class="brand brand--faint-top">Venture Kite</div>
    <div class="brand brand--faint-bottom">Venture Kite</div>

    <div class="contact contact--primary">
      <p class="contact-name">Ha Min Park</p>
      <p class="contact-role">Project Leader</p>
      <p class="contact-line">M : 047- 720- 3941</p>
      <p class="contact-line">E : ha-min.park@corvalaktrb.org</p>
      <p class="contact-line">W : www.corvalaktrb.org</p>
    </div>

    <div class="contact contact--secondary">
      <p class="contact-name">Thomas Leung</p>
      <p class="contact-role">Vice Project Leader</p>
      <p class="contact-line">M : 047- 935- 2806</p>
      <p class="contact-line">E : thomas.leung@corvalaktrb.org</p>
      <p class="contact-line">W : www.corvalaktrb.org</p>
    </div>
  </section>

</main>
</body>
</html>
```